Logo and 1 page Flyer for Meadowlark Fund

We need a logo and a 1 single page flyer for an Investment Fund we'll distribute worldwide. It'a Meadowlark Fund that will give a return also to the poorest people in the world. Details inside. We give just an idea (based on a previous flyer we had here) with the attached draft. Anyone can figure out how to make its own. NOTE: TQV is our company's logo.

Target Market(s)

Investors

Industry/Entity Type

Finance And Accounting

Logo Text

KELP Kindred Open Grow Fund

Font styles to use
Serif

Colors
00a990

Requirements
Must have
• A logo you choose which should be:
• - Elegant
• - Innovative
• - Crypto evoking (Company launching is a cripto company)
• - Hi tech
Nice to have
• We have sent you all materials to be able to understand:
• 1. A draft of how we would like the texts to come out. Don't use this (we're already using with other texts), ,but see the evidence of Logo, Slogan, and the 3 main characteristics. Also notice very well that is very elegant. Use a real light on color, make it as shining as you can. It must be a sort of shining green, expressing Hope, Beauty, Well being
• 2. The logo for TQV that is the company launching the project. In draft you see on low left. You can put wherever you feel right
• 3. All texts are on draft to be seen, and on word to be used. You can choose font and dimensions as you prefer
• 4. We've given you logo we have for PLOM. If you feel, you can use in the line where we talk about it or place somewhere. Not mandatory
Should not have
• Funny things; too commercial style; unprofessional aspect

```html
<!DOCTYPE html>
<html lang="en">
<head>
<meta charset="utf-8">
<title>KELP – Kindred Open Grow Fund</title>
<link href="https://fonts.googleapis.com/css2?family=Lora:wght@400;700&family=Playfair+Display:wght@700;800;900&display=swap" rel="stylesheet">
<style>
  :root {
    --brand-green: #00a990;
    --deep-green: #007a68;
    --dark-green: #00564a;
    --mid-green: #1fbfa3;
    --light-green: #6ee0c9;
    --glow-green: #d9fff6;
    --mint-tint: #d9f3ee;
    --ink: #2f3a38;
    --night: #031310;
    --pill-grey: #4f5a58;
    --white: #ffffff;
  }
  html, body {
    margin: 0;
    padding: 0;
    width: 970px;
    height: 1200px;
    overflow: hidden;
    background: var(--white);
  }
  .flyer {
    position: relative;
    width: 970px;
    height: 1200px;
    overflow: hidden;
    font-family: "Lora", Georgia, serif;
    background: linear-gradient(90deg, var(--mint-tint) 0%, var(--white) 14%, var(--white) 86%, var(--mint-tint) 100%);
  }
  .hero {
    position: absolute;
    left: 0;
    top: 0;
    width: 970px;
    height: 600px;
    clip-path: path('M0,0 H970 V598 Q485,500 0,598 Z');
  }
  .hero-shapes {
    position: absolute;
    inset: 0;
    width: 970px;
    height: 600px;
  }
  .hero-visual {
    position: absolute;
    inset: 0;
    clip-path: polygon(236px 0, 970px 0, 970px 490px, 660px 455px, 511px 545px);
    background:
      radial-gradient(circle at 652px 232px, var(--glow-green) 0, var(--light-green) 40px, var(--brand-green) 100px, #0a4d42 180px, #05231e 260px, var(--night) 340px);
  }
  .brand {
    position: absolute;
    left: 55px;
    top: 150px;
    width: 270px;
    text-align: center;
    color: var(--white);
    font-family: "Playfair Display", Georgia, serif;
    font-weight: 800;
  }
  .brand-mark {
    display: block;
    width: 130px;
    height: 130px;
    margin: 0 auto 42px;
    border: 5px solid var(--white);
    border-radius: 50%;
    box-sizing: border-box;
  }
  .brand-name {
    display: block;
    font-size: 92px;
    line-height: 0.85;
    letter-spacing: 1px;
  }
  .brand-tagline {
    display: block;
    margin-top: 12px;
    font-size: 17px;
    letter-spacing: 2px;
  }
  .headline {
    position: absolute;
    left: 0;
    right: 0;
    top: 674px;
    margin: 0;
    text-align: center;
    color: var(--brand-green);
    font-family: "Playfair Display", Georgia, serif;
    font-weight: 800;
    font-size: 64px;
    line-height: 68px;
  }
  .intro {
    position: absolute;
    left: 0;
    right: 0;
    top: 824px;
    margin: 0;
    text-align: center;
    color: var(--ink);
    font-size: 17px;
    line-height: 23px;
  }
  .features {
    position: absolute;
    left: 30px;
    right: 30px;
    top: 915px;
    display: flex;
    margin: 0;
    padding: 0;
    list-style: none;
  }
  .feature {
    flex: 1;
    height: 118px;
    text-align: center;
  }
  .feature + .feature {
    border-left: 2.5px solid var(--ink);
  }
  .feature-title {
    margin: 6px 0 14px;
    color: var(--brand-green);
    font-family: "Playfair Display", Georgia, serif;
    font-weight: 700;
    font-size: 22px;
  }
  .feature-text {
    margin: 0;
    color: var(--ink);
    font-size: 16.5px;
    line-height: 23px;
  }
  .site-tab {
    position: absolute;
    left: 321px;
    top: 1128px;
    width: 330px;
    height: 56px;
    border-radius: 44px 44px 0 0;
    background: var(--pill-grey);
    color: var(--white);
    text-align: center;
    font-size: 26px;
    line-height: 54px;
    letter-spacing: 0.5px;
  }
  .footer-band {
    position: absolute;
    left: 0;
    bottom: 0;
    width: 970px;
    height: 20px;
    background: linear-gradient(90deg, var(--deep-green), var(--light-green) 25%, var(--deep-green) 50%, var(--brand-green));
  }
</style>
</head>
<body>
<main class="flyer">
  <div class="hero">
    <svg class="hero-shapes" viewBox="0 0 970 600" aria-hidden="true">
      <rect width="970" height="600" fill="#009a83"/>
      <polygon points="0,0 60,0 0,60" fill="#5fd6bf"/>
      <polygon points="60,0 236,0 0,180 0,60" fill="#00846f"/>
      <polygon points="0,180 236,0 360,330 0,600" fill="#00a990"/>
      <polygon points="120,500 360,330 511,545 200,600" fill="#3fc7ad" opacity="0.75"/>
      <polygon points="0,600 120,500 200,600" fill="#8fe8d6"/>
      <polygon points="470,470 560,455 660,455 600,545 520,560" fill="#0d1a18"/>
      <polygon points="490,462 660,455 630,480 505,480" fill="#b8c4c1"/>
      <polygon points="660,455 970,490 970,600 720,600" fill="#00846f"/>
      <polygon points="600,500 700,470 760,560 620,580" fill="#1fbfa3"/>
    </svg>
    <div class="hero-visual" role="img" aria-label="Glowing digital coin at the centre of a circuit board on a dark background"></div>
  </div>

  <div class="brand">
    <span class="brand-mark"></span>
    <span class="brand-name">KELP</span>
    <span class="brand-tagline">Kindred Open Grow Fund</span>
  </div>

  <h1 class="headline">Raise The Poor<br>Surfing With Us</h1>
  <p class="intro">With KELP you achieve sound return on your investment. And you help needy<br>ones to obtain real help in their life.</p>

  <ul class="features">
    <li class="feature">
      <h2 class="feature-title">Better RETURN</h2>
      <p class="feature-text">Using PLOM – Highly Advanced<br>Trading System. A breakthrough<br>in money management</p>
    </li>
    <li class="feature">
      <h2 class="feature-title">For ANYONE</h2>
      <p class="feature-text">For those who can invest.<br>And for those Who have no<br>money to survive.</p>
    </li>
    <li class="feature">
      <h2 class="feature-title">Money and HEARTH</h2>
      <p class="feature-text">To have a return that<br>Warms you and others.</p>
    </li>
  </ul>

  <div class="site-tab">www.tqvf.io</div>
  <div class="footer-band"></div>
</main>
</body>
</html>
```